Flask Up Fable needs wedding label designs!

Flask Up Fable is looking for new wedding designs! Please look at http://www.flaskupfable.com/water-bottle-labels and http://www.flaskupfable.com/custom-water to get an idea of what we currently offer.

These new designs will be saved onto Flask Up Fable so that customers can come and customize the text and/or add pictures on them for purchase as water bottle labels or custom label bottled water.

Designs must appeal to a broad audience so any and all styles will be considered. Some other sites to draw inspiration from are plumquill.com, velcrest.com, vowsheetmuses.com and ferlow.com.

Questions? Ask away!

Target Market(s)

Target market is brides, mothers of brides and wedding planners.

Industry/Entity Type

Wedding

Requirements
Must have
• Designs must be at 300 dpi in CMYK. Width is 8.133" Height is 2.377" with a .125" bleed around all sides.

```html
<!DOCTYPE html>
<html lang="en">
<head>
<meta charset="utf-8">
<title>Wedding Water Bottle Labels</title>
<link rel="stylesheet" href="https://fonts.googleapis.com/css2?family=PT+Sans:ital,wght@1,700&family=Lora:ital,wght@1,700&display=swap">
<style>
  :root {
    --page-bg: #f2f2f2;
    --cream: #ebe6cf;
    --cream-light: #f3efdc;
    --cream-deep: #ddd5b4;
    --olive: #b6a766;
    --olive-text: #9c8b45;
    --teal: #4f7f86;
    --teal-soft: #8fb0b3;
    --coral: #ef7b52;
    --coral-deep: #e0603a;
    --coral-light: #f49a72;
    --red: #c9252b;
    --white: #ffffff;
  }
  * { margin: 0; padding: 0; box-sizing: border-box; }
  html, body {
    width: 1200px;
    height: 900px;
    overflow: hidden;
    background: var(--page-bg);
  }
  .canvas {
    width: 1200px;
    height: 900px;
    display: flex;
    flex-direction: column;
    align-items: center;
    justify-content: center;
    gap: 110px;
  }
  .label {
    display: block;
    width: 900px;
    height: 263px;
    box-shadow: 0 2px 10px rgba(0, 0, 0, 0.12);
  }
  .name-classic {
    font-family: "PT Sans", sans-serif;
    font-style: italic;
    font-weight: 700;
    fill: var(--olive-text);
  }
  .name-scroll {
    font-family: "Lora", serif;
    font-style: italic;
    font-weight: 700;
    fill: var(--red);
  }
</style>
</head>
<body>
<main class="canvas">

  <!-- Cream floral label -->
  <svg class="label label-cream" viewBox="0 0 900 263" xmlns="http://www.w3.org/2000/svg">
    <defs>
      <linearGradient id="creamFloral" x1="0" y1="0" x2="1" y2="1">
        <stop offset="0" stop-color="var(--cream-light)"/>
        <stop offset="0.5" stop-color="var(--cream)"/>
        <stop offset="1" stop-color="var(--cream-deep)"/>
      </linearGradient>
    </defs>
    <rect class="floral-background" role="img" aria-label="Soft cream floral pattern" width="900" height="263" fill="url(#creamFloral)"/>
    <g class="stripes-top">
      <rect y="66" width="900" height="12" fill="var(--olive)"/>
      <rect y="78" width="900" height="8" fill="var(--teal)"/>
    </g>
    <g class="stripes-bottom">
      <rect y="172" width="900" height="8" fill="var(--teal)"/>
      <rect y="180" width="900" height="12" fill="var(--olive)"/>
    </g>
    <rect class="ornament ornament-left" role="img" aria-label="Teal three-leaf ornament" x="20" y="95" width="68" height="68" rx="34" fill="var(--teal-soft)" opacity="0.6"/>
    <rect class="ornament ornament-right" role="img" aria-label="Teal three-leaf ornament" x="812" y="95" width="68" height="68" rx="34" fill="var(--teal-soft)" opacity="0.6"/>
    <text class="name-classic couple" x="450" y="134" font-size="36" text-anchor="middle">Clara &amp; Daniel</text>
    <text class="name-classic date" x="450" y="160" font-size="18" text-anchor="middle">May 15, 2011</text>
  </svg>

  <!-- Coral scroll label -->
  <svg class="label label-coral" viewBox="0 0 900 263" xmlns="http://www.w3.org/2000/svg">
    <defs>
      <linearGradient id="coralScroll" x1="0" y1="0" x2="1" y2="1">
        <stop offset="0" stop-color="var(--coral-light)"/>
        <stop offset="0.5" stop-color="var(--coral)"/>
        <stop offset="1" stop-color="var(--coral-deep)"/>
      </linearGradient>
    </defs>
    <rect class="scroll-background" role="img" aria-label="Red flourish scroll pattern on coral" width="900" height="263" fill="url(#coralScroll)"/>
    <ellipse class="name-oval" cx="450" cy="131" rx="152" ry="84" fill="var(--white)" stroke="var(--red)" stroke-width="9"/>
    <text class="name-scroll couple" x="450" y="130" font-size="34" text-anchor="middle">Clara &amp; Daniel</text>
    <text class="name-scroll date" x="450" y="160" font-size="18" text-anchor="middle">May 15, 2011</text>
  </svg>

</main>
</body>
</html>
```